Maple Ridge Hops Farm

We need a business card with some pizam in it. Our slogan is something different so something a little different would do!

Business

```html
<!DOCTYPE html>
<html lang="en">
<head>
<meta charset="utf-8">
<title>Maple Ridge Hops Farm — Business Card</title>
<link rel="stylesheet" href="https://fonts.googleapis.com/css2?family=Saira+Condensed:wght@600;700&family=Play:wght@400;700&display=swap">
<style>
  :root {
    --stage: #e9e6de;
    --card-white: #ffffff;
    --card-grey: #dcdcdc;
    --olive: #5a6421;
    --olive-dark: #4c551b;
    --lime: #a3b84f;
    --ink: #4b4b3c;
    --name: #5a6421;
    --light-text: #f4f4ec;
  }
  * { box-sizing: border-box; margin: 0; padding: 0; }
  html, body {
    width: 1200px;
    height: 1019px;
    overflow: hidden;
    background: var(--stage);
  }
  .stage {
    width: 1200px;
    height: 1019px;
    display: flex;
    align-items: center;
    justify-content: center;
  }
  .card {
    width: 1000px;
    height: 571px;
    display: flex;
    flex-direction: column;
    box-shadow: 0 18px 40px rgba(60, 50, 30, 0.25);
    overflow: hidden;
  }
  .card__top {
    flex: 0 0 330px;
    background: radial-gradient(ellipse at 62% 70%, var(--card-white) 0%, #f2f2f2 45%, var(--card-grey) 100%);
    display: flex;
    align-items: center;
    justify-content: space-between;
    padding: 0 70px 0 60px;
  }
  .brand {
    display: flex;
    align-items: center;
    gap: 18px;
  }
  .brand__dot {
    width: 46px;
    height: 46px;
    border-radius: 50%;
    background: var(--olive);
    flex: none;
  }
  .brand__name {
    font-family: "Saira Condensed", sans-serif;
    font-weight: 700;
    font-size: 44px;
    line-height: 1;
    color: var(--olive);
    text-transform: uppercase;
    max-width: 260px;
  }
  .person {
    align-self: flex-end;
    margin-bottom: 40px;
    text-align: left;
  }
  .person__name {
    font-family: "Saira Condensed", sans-serif;
    font-weight: 700;
    font-size: 74px;
    line-height: 0.9;
    color: var(--name);
    letter-spacing: 1px;
  }
  .person__role {
    font-family: "Play", sans-serif;
    font-size: 26px;
    letter-spacing: 3px;
    color: var(--ink);
    margin-top: 4px;
  }
  .card__bottom {
    flex: 1;
    background: var(--olive);
    padding: 34px 0 0 0;
  }
  .labels {
    display: flex;
    align-items: center;
    height: 50px;
  }
  .labels__rule {
    height: 10px;
    background: var(--lime);
  }
  .labels__rule--lead { width: 40px; margin-right: 20px; }
  .labels__rule--mid { flex: 1; margin: 0 22px; }
  .labels__rule--tail { width: 140px; margin-left: 22px; }
  .label {
    font-family: "Saira Condensed", sans-serif;
    font-weight: 700;
    font-size: 50px;
    line-height: 1;
    color: var(--light-text);
  }
  .details {
    display: flex;
    padding: 22px 0 0 60px;
    gap: 0;
  }
  .details__col {
    font-family: "Play", sans-serif;
    font-size: 22px;
    line-height: 1.45;
    color: var(--light-text);
    letter-spacing: 1px;
  }
  .details__col--address { width: 330px; }
  .details__col--phone { width: 260px; }
  .details__col--email { width: 350px; }
</style>
</head>
<body>
<main class="stage">
  <article class="card">
    <section class="card__top">
      <div class="brand">
        <span class="brand__dot"></span>
        <span class="brand__name">Maple Ridge Hops Farm</span>
      </div>
      <div class="person">
        <h1 class="person__name">EVAN HOLLIS</h1>
        <p class="person__role">GENERAL MANAGER</p>
      </div>
    </section>
    <section class="card__bottom">
      <div class="labels">
        <span class="labels__rule labels__rule--lead"></span>
        <span class="label">ADDRESS</span>
        <span class="labels__rule labels__rule--mid"></span>
        <span class="label">PHONE</span>
        <span class="labels__rule labels__rule--mid"></span>
        <span class="label">EMAIL</span>
        <span class="labels__rule labels__rule--tail"></span>
      </div>
      <div class="details">
        <p class="details__col details__col--address">41 Orchard Lane,<br>Ridgeview Valley</p>
        <p class="details__col details__col--phone">555 014 2290<br>555 014 2291</p>
        <p class="details__col details__col--email">evan@mapleridgehops.com<br>www.mapleridgehops.com</p>
      </div>
    </section>
  </article>
</main>
</body>
</html>
```